Cover Art Design for a Notebook

We are going to give away some note books to our marketing department and want an elegant art design for the cover. There is a theme centered around ABCD of marketing that we want to leverage in the design. So these letters should be prominent in the design. The ABCD stand for Agility, Boost, Customer, Data.

If you could Cleverly incorporate these words into the letters with a good design that would be good.

But please make the ABCD the focus of the artwork. The words associated with them should be subtle, in the background, visible but not the focus.

We are looking for stylish. We want people to feel proud of the ELEGANT DESIGN when they take out this notebook for business.

Also worth mentioning- We are a biotechnology company so if you incorporate elements in that theme in, on, or around the ABCD letters, it could be a good idea. As long as it doesn’t kill the rest of the design.

I will upload our logo for Veltrane Orwick Biologics later (you can see it online) and this will need to go in one corner.

Notebook will be A5 format. Image on front cover only. Need ASAP.

(Do not make baby blocks as we don’t want something that looks like a kids book)

Target Market(s)

business people who feel proud to pull out this notebook

Industry/Entity Type

Biotechnology

Colors
ec1f27
ffffff
000000

Requirements
Must have
• ELEGANT ART DESIGN USING ABCD
Nice to have
• see brief above
Should not have
• baby blocks

```html
<!DOCTYPE html>
<html lang="en">
<head>
<meta charset="utf-8">
<title>ABCD Notebook Cover</title>
<link rel="stylesheet" href="https://fonts.googleapis.com/css2?family=Montserrat:wght@500;600;700&display=swap">
<style>
  :root {
    --cover-white: #f4f4f4;
    --quilt-shade: #e2e2e2;
    --gold: #c9a04e;
    --brand-red: #ec1f27;
    --ink: #000000;
  }
  * { margin: 0; padding: 0; box-sizing: border-box; }
  html, body {
    width: 1200px;
    height: 2552px;
    overflow: hidden;
  }
  body {
    position: relative;
    font-family: "Montserrat", sans-serif;
    background: var(--brand-red);
  }
  .cover {
    position: absolute;
    left: 0; top: 0;
    width: 1200px;
    height: 1692px;
  }
  .cover__texture {
    position: absolute;
    inset: 0;
    background: radial-gradient(ellipse at 50% 40%, #ffffff 0%, var(--cover-white) 55%, var(--quilt-shade) 100%);
  }
  .monogram {
    position: absolute;
    left: 0; top: 0;
    width: 1200px;
    height: 1692px;
  }
  .monogram__letter {
    position: absolute;
    left: 490px;
    width: 220px;
    text-align: center;
    font-weight: 700;
    font-size: 330px;
    line-height: 1;
    color: var(--gold);
  }
  .monogram__word {
    position: absolute;
    font-weight: 500;
    font-size: 30px;
    line-height: 36px;
    height: 36px;
    letter-spacing: 3px;
    color: var(--gold);
    transform: rotate(-90deg);
    transform-origin: left top;
    white-space: nowrap;
  }
  .letter-a { top: 190px; }
  .letter-b { top: 475px; }
  .letter-c { top: 765px; }
  .letter-d { top: 1060px; }
  .word-agility { left: 440px; top: 400px; }
  .word-boost { left: 468px; top: 720px; }
  .word-customer { left: 440px; top: 1030px; }
  .word-data { left: 468px; top: 1330px; }
  .brand-mark {
    position: absolute;
    left: 880px;
    top: 1590px;
    width: 290px;
    text-align: center;
    font-weight: 600;
    font-size: 30px;
    line-height: 1.15;
    color: var(--brand-red);
  }
  .base-band {
    position: absolute;
    left: 0; top: 1692px;
    width: 1200px;
    height: 860px;
    background: var(--brand-red);
  }
</style>
</head>
<body>
  <section class="cover">
    <div class="cover__texture" role="img" aria-label="White quilted diamond padding texture"></div>
    <div class="monogram">
      <div class="monogram__letter letter-a">A</div>
      <div class="monogram__word word-agility">AGILITY</div>
      <div class="monogram__letter letter-b">B</div>
      <div class="monogram__word word-boost">BOOST</div>
      <div class="monogram__letter letter-c">C</div>
      <div class="monogram__word word-customer">CUSTOMER</div>
      <div class="monogram__letter letter-d">D</div>
      <div class="monogram__word word-data">DATA</div>
    </div>
    <div class="brand-mark">Veltrane Orwick<br>Biologics</div>
  </section>
  <div class="base-band"></div>
</body>
</html>
```